Modern business card design for professional copywriter

I'd like a business card design that I can use to have my cards printed out by plink.com as a squared corners business card (see artwork and design guidelines here: https://help.plink.com/hc/en-gb/sections/300481726-PLINK-Product-Templates)

The design should be clean and modern and reflect the colours, tone and branding on my website: https://noravestrel.com.au

Target Market(s)

Professionals, B2B small business owners

Industry/Entity Type

Business

Contact Information for Business Card

Nora Vestrel
m: 0427 593 864
e: nora@noravestrel.com.au
w: noravestrel.com.au

Font styles to use
Sans Serif

Requirements
Must have
• Tagline: "Smart copywriting for clever business people"
• Brand colours: fd8000, 009984, 666666 and black
Nice to have

```html
<!DOCTYPE html>
<html lang="en">
<head>
<meta charset="utf-8">
<title>Nora Vestrel – Business Card</title>
<link rel="stylesheet" href="https://fonts.googleapis.com/css2?family=Montserrat:wght@500;700&family=Didact+Gothic&display=swap">
<style>
  :root {
    --brand-orange: #fd8000;
    --brand-teal: #009984;
    --brand-grey: #666666;
    --ink: #000000;
    --card: #ffffff;
    --backdrop: #e9e9e7;
    --faint-orange: rgba(253, 128, 0, 0.06);
  }
  * { margin: 0; padding: 0; box-sizing: border-box; }
  html, body {
    width: 1200px;
    height: 810px;
    overflow: hidden;
    background: var(--backdrop);
  }
  .stage {
    position: relative;
    width: 1200px;
    height: 810px;
  }
  .card {
    position: absolute;
    width: 520px;
    height: 336px;
    background: var(--card);
    box-shadow: 0 2px 10px rgba(0, 0, 0, 0.12);
    overflow: hidden;
  }
  .card--front { left: 60px; top: 120px; }
  .card--back { left: 620px; top: 354px; }

  .wordmark {
    display: flex;
    align-items: center;
    gap: 10px;
    font-family: "Montserrat", sans-serif;
    font-weight: 500;
    color: var(--brand-teal);
    letter-spacing: -0.5px;
  }
  .wordmark__dot {
    width: 14px;
    height: 14px;
    border-radius: 50%;
    background: var(--brand-orange);
  }

  .card--front .wordmark {
    position: absolute;
    left: 0;
    right: 0;
    top: 112px;
    justify-content: center;
    font-size: 40px;
  }
  .tagline {
    position: absolute;
    left: 0;
    right: 0;
    bottom: 58px;
    text-align: center;
    font-family: "Didact Gothic", sans-serif;
    font-size: 13px;
    color: var(--brand-grey);
    letter-spacing: 0.3px;
  }

  .card--back .wordmark {
    position: absolute;
    left: 36px;
    top: 88px;
    font-size: 28px;
  }
  .card__decor {
    position: absolute;
    right: 60px;
    top: 40px;
    width: 200px;
    height: 200px;
    border-radius: 50%;
    background: var(--faint-orange);
  }
  .contact {
    position: absolute;
    right: 36px;
    top: 168px;
    width: 200px;
    font-family: "Didact Gothic", sans-serif;
  }
  .contact__name {
    font-family: "Montserrat", sans-serif;
    font-weight: 700;
    font-size: 19px;
    color: var(--brand-teal);
    margin-bottom: 6px;
  }
  .contact__list { list-style: none; }
  .contact__item {
    display: flex;
    align-items: center;
    gap: 6px;
    font-size: 12.5px;
    color: var(--brand-grey);
    line-height: 22px;
  }
  .contact__icon {
    width: 11px;
    height: 11px;
    flex: none;
    fill: var(--brand-orange);
  }
</style>
</head>
<body>
<main class="stage">
  <section class="card card--front" aria-label="Card front">
    <div class="wordmark"><span class="wordmark__dot"></span>Nora Vestrel</div>
    <p class="tagline">Smart copywriting for clever business people</p>
  </section>

  <section class="card card--back" aria-label="Card back">
    <div class="card__decor" aria-hidden="true"></div>
    <div class="wordmark"><span class="wordmark__dot"></span>Nora Vestrel</div>
    <div class="contact">
      <p class="contact__name">Nora Vestrel</p>
      <ul class="contact__list">
        <li class="contact__item">
          <svg class="contact__icon" viewBox="0 0 24 24" aria-hidden="true"><path d="M6.6 10.8a15.1 15.1 0 0 0 6.6 6.6l2.2-2.2a1 1 0 0 1 1-.25 11.4 11.4 0 0 0 3.6.57 1 1 0 0 1 1 1V20a1 1 0 0 1-1 1A17 17 0 0 1 3 4a1 1 0 0 1 1-1h3.5a1 1 0 0 1 1 1c0 1.25.2 2.45.57 3.6a1 1 0 0 1-.25 1z"/></svg>
          0427 593 864
        </li>
        <li class="contact__item">
          <svg class="contact__icon" viewBox="0 0 24 24" aria-hidden="true"><path d="M2 5h20v14H2z M2 5l10 8 10-8" fill="none" stroke="var(--brand-orange)" stroke-width="2.5"/></svg>
          nora@noravestrel.com.au
        </li>
        <li class="contact__item">
          <svg class="contact__icon" viewBox="0 0 24 24" aria-hidden="true"><circle cx="12" cy="12" r="10" fill="none" stroke="var(--brand-orange)" stroke-width="2.5"/><path d="M2 12h20M12 2c3 3 3 17 0 20M12 2c-3 3-3 17 0 20" fill="none" stroke="var(--brand-orange)" stroke-width="2"/></svg>
          noravestrel.com.au
        </li>
      </ul>
    </div>
  </section>
</main>
</body>
</html>
```